Lumara Health & Wellness Business Card Design

We would like to create business cards matching with our new logo design. The card should be professional looking but still have a playful side and something that would be eye catching. We are planing to open a luxury medical spa and looking to create a design based on this new logo. We are looking for a design that shows off luxury but not be gold in color. Also, while we are a more female oriented medical center we do have men that come in for our services and it should be be too feminine.

Target Market(s)

Health & Wellness. Medical patients. Luxury spa

Industry/Entity Type

Health And Wellness

Contact Information for Business Card

It should have the logo design in the front of card and back of card should have our contact information. Our current colors are peach/ coral, teal, and gray. We are looking for a modern looking design.

Font styles to use
Script

Colors
32a6d6
e667a6
86cfc6
fece3e

Requirements
Must have
• It should have our logo design. We would prefer to have a more modern look to the card.
Nice to have
• Eye-Catching Design on the personable side but still classy.
Should not have
• At this point we are looking for the best design. It should not have color purple.

```html
<!DOCTYPE html>
<html lang="en">
<head>
<meta charset="utf-8">
<title>Lumara Health &amp; Wellness – Business Card</title>
<link rel="stylesheet" href="https://fonts.googleapis.com/css2?family=Lato:wght@400;700&display=swap">
<style>
  :root {
    --backdrop: #cbcbcb;
    --card-dark: #0c0c0c;
    --wedge-gray: #7a7a7a;
    --card-light: #ffffff;
    --ink-light: #ffffff;
    --ink-dark: #111111;
  }
  html, body {
    margin: 0;
    padding: 0;
    width: 1200px;
    height: 802px;
    overflow: hidden;
    background: var(--backdrop);
    font-family: "Lato", sans-serif;
  }
  .canvas {
    position: relative;
    width: 1200px;
    height: 802px;
  }
  .card {
    position: absolute;
    top: 274px;
    width: 443px;
    height: 264px;
    overflow: hidden;
  }
  .card--contact {
    left: 136px;
    background: var(--card-dark);
    color: var(--ink-light);
  }
  .card--brand {
    left: 624px;
    background: var(--card-light);
    color: var(--ink-dark);
  }
  .wedge {
    position: absolute;
    inset: 0;
    width: 100%;
    height: 100%;
  }
  .wedge polygon { fill: var(--wedge-gray); }
  .details {
    position: absolute;
    right: 25px;
    top: 56px;
    text-align: right;
  }
  .details__name {
    margin: 0;
    font-size: 16.5px;
    font-weight: 700;
    letter-spacing: 0.4px;
    line-height: 18px;
    text-transform: uppercase;
  }
  .details__role {
    margin: 0 0 10px;
    font-size: 12px;
    line-height: 14px;
  }
  .contact-list {
    list-style: none;
    margin: 0 0 9px;
    padding: 0;
  }
  .contact-list li {
    display: flex;
    justify-content: flex-end;
    align-items: center;
    gap: 4px;
    font-size: 11.5px;
    line-height: 16px;
  }
  .contact-list svg {
    width: 9px;
    height: 9px;
    fill: var(--ink-light);
  }
  .address {
    margin: 0;
    font-style: normal;
    font-size: 12px;
    line-height: 16px;
    padding-right: 13px;
  }
  .brand-name {
    position: absolute;
    left: 0;
    right: 0;
    top: 120px;
    margin: 0;
    text-align: center;
    font-size: 20px;
    font-weight: 400;
    letter-spacing: 0.5px;
    color: var(--ink-dark);
  }
</style>
</head>
<body>
<main class="canvas">
  <section class="card card--contact" aria-label="Business card, contact side">
    <svg class="wedge" viewBox="0 0 443 264" preserveAspectRatio="none" aria-hidden="true">
      <polygon points="0,0 222,0 15,264 0,264"/>
    </svg>
    <div class="details">
      <h1 class="details__name">Dorian Hale</h1>
      <p class="details__role">Managing Director</p>
      <ul class="contact-list">
        <li>044-555 210 347
          <svg viewBox="0 0 10 10" aria-label="phone"><path d="M1 3c0-1.2 1-2 4-2s4 .8 4 2v1H7V3H3v1H1zM2 5h6l1 4H1z"/></svg>
        </li>
        <li>044-555 210 347
          <svg viewBox="0 0 10 10" aria-label="mobile"><path d="M3 0h4a1 1 0 0 1 1 1v8a1 1 0 0 1-1 1H3a1 1 0 0 1-1-1V1a1 1 0 0 1 1-1zm.2 1.2v6.6h3.6V1.2z"/></svg>
        </li>
        <li>hello@lumarahealth.com
          <svg viewBox="0 0 10 10" aria-label="email"><path d="M0 2h10v6H0zM1 2.8v.4L5 5.6l4-2.4v-.4z"/></svg>
        </li>
        <li>www.lumarahealth.com
          <svg viewBox="0 0 10 10" aria-label="website"><circle cx="5" cy="5" r="4.6"/></svg>
        </li>
      </ul>
      <address class="address">4820 Harbor Lane<br>Westport, 604512</address>
    </div>
  </section>

  <section class="card card--brand" aria-label="Business card, brand side">
    <p class="brand-name">Lumara Health &amp; Wellness</p>
  </section>
</main>
</body>
</html>
```